Certified Public Accountant specializing in tax preparation.

I need a business card designed that conveys knowledgeability, trustworthiness and competency. I am a licensed CPA and hold a Master's in taxation. As this is a personal service business, I would like to include my picture on the card.

```html
<!DOCTYPE html>
<html lang="en">
<head>
<meta charset="utf-8">
<title>Laura Pemberton – Business Card</title>
<link rel="stylesheet" href="https://fonts.googleapis.com/css2?family=Arimo:wght@400;700&display=swap">
<style>
  :root {
    --backdrop: #e4e4e4;
    --card: #ffffff;
    --brand-brown: #4a1f1a;
    --body-text: #1a1a1a;
    --portrait-upper: #8a6453;
    --portrait-lower: #e6c6d4;
  }
  * { margin: 0; padding: 0; box-sizing: border-box; }
  html, body {
    width: 1200px;
    height: 791px;
    overflow: hidden;
    background: var(--backdrop);
    font-family: "Arimo", Arial, sans-serif;
  }
  .business-card {
    position: absolute;
    left: 158px;
    top: 142px;
    width: 882px;
    height: 503px;
    background: var(--card);
    border-radius: 24px;
    overflow: hidden;
  }
  .accent-bar {
    position: absolute;
    left: 0;
    top: 243px;
    width: 13px;
    height: 66px;
    background: var(--brand-brown);
  }
  .identity {
    position: absolute;
    left: 66px;
    top: 240px;
    color: var(--brand-brown);
  }
  .identity .name {
    font-size: 33px;
    font-weight: 700;
    line-height: 36px;
  }
  .identity .credential {
    font-size: 22px;
    font-weight: 400;
    line-height: 26px;
  }
  .contact-list {
    position: absolute;
    left: 68px;
    top: 329px;
    list-style: none;
    color: var(--body-text);
    font-size: 20px;
    line-height: 26px;
  }
  .contact-list li {
    display: flex;
    align-items: center;
    gap: 9px;
  }
  .contact-list svg {
    width: 20px;
    height: 20px;
    fill: var(--brand-brown);
    flex: none;
  }
  .license {
    position: absolute;
    left: 66px;
    top: 427px;
    font-size: 20px;
    line-height: 24px;
    font-weight: 700;
    color: var(--brand-brown);
  }
  .portrait {
    position: absolute;
    left: 467px;
    top: 26px;
    width: 392px;
    height: 477px;
    background: linear-gradient(180deg, var(--portrait-upper) 0%, var(--portrait-lower) 100%);
  }
</style>
</head>
<body>
  <article class="business-card">
    <div class="accent-bar"></div>

    <header class="identity">
      <h1 class="name">Laura Pemberton</h1>
      <p class="credential">Master's in taxation</p>
    </header>

    <ul class="contact-list">
      <li>
        <svg viewBox="0 0 24 24" aria-hidden="true"><path d="M6.6 10.8a15.1 15.1 0 0 0 6.6 6.6l2.2-2.2c.3-.3.7-.4 1-.2 1.1.4 2.3.6 3.6.6.6 0 1 .4 1 1V20c0 .6-.4 1-1 1A17 17 0 0 1 3 4c0-.6.4-1 1-1h3.5c.6 0 1 .4 1 1 0 1.3.2 2.5.6 3.6.1.3 0 .7-.2 1z"/></svg>
        <span>555 214 7390</span>
      </li>
      <li>
        <svg viewBox="0 0 24 24" aria-hidden="true"><path d="M2 5h20v14H2z M3.5 6.5 12 12.5l8.5-6v1.7L12 14.2 3.5 8.2z" fill-rule="evenodd"/></svg>
        <span>laura@ledgerline.com</span>
      </li>
      <li>
        <svg viewBox="0 0 24 24" aria-hidden="true"><circle cx="12" cy="12" r="10"/><path d="M7 6c2 1 3 3 2 5s1 3 2 4-1 4-1 5M15 4c-1 2 1 3 3 4s1 4 3 5" stroke="#fff" stroke-width="1.6" fill="none"/></svg>
        <span>www.ledgerline.com</span>
      </li>
    </ul>

    <p class="license">Licensed CPA</p>

    <div class="portrait" role="img" aria-label="Portrait photo of the accountant"></div>
  </article>
</body>
</html>
```